I am writing a book called "SMILING OPENS EVERY DOOR "

I NEED A BOOK COVER FOR MY BOOK" SMILING OPENS EVERY DOOR"
so what was the question? " ( this in smaller font)

"Smiling Opens Every Door " will need to designed to eventually be a logo , banner and business card
COLOURS MAINLY ORANGE AND WHITE (with accents bright colour )

THE BOOK IS MY LAUGHTER JOURNEY AS A PERFORMER AND ADVENTURE INDIA LEARNING ABOUT LAUGHTER YOGA WHICH I WILL BE TEACHING

I do not want photos on the front cover ..
The look could be modern and eye-catching
I have also just been to India to learn Laughing Yoga with Dr Tobin Verhaal

Thank-you so much everyone for your brilliant designs . i am overwhelmed with your talent . i hope to work with you all again soon ! Marnie  

Target Market(s)

"Adults based in western speaking countries aged 25 to 60 that want to learn to laugh more
Also this book will be sold at my conference workshops

Industry/Entity Type

Business

Requirements
Must have
• ORANGE AND WHITE
CAN HAVE AQUA , HOT PINK , LIME GREEN, YELLOW ACCENTS

THESE WILL BE DIFFERENT AREAS WILL COVERING IN MY BOOK
EG LAUGHTER NAD BREAT CANCER ( PINK)
LAUGHTER NAD DEPRESSION ( BLUE)
LAUGHTER AND KIDS ( YELLOW)

NO Photos on front cover
Should not have
• No photos

```html
<!DOCTYPE html>
<html lang="en">
<head>
<meta charset="utf-8">
<title>Smiling Opens Every Door — Book Cover</title>
<link rel="stylesheet" href="https://fonts.googleapis.com/css2?family=Audiowide&family=Open+Sans:wght@400;700;800&display=swap">
<style>
  :root {
    --orange-core: #f7784a;
    --orange-mid: #f2603a;
    --orange-edge: #e9441f;
    --white: #ffffff;
    --yellow: #ffde17;
    --smile-yellow: #ffd60a;
    --band-pink: #e8306a;
    --band-text: #f6a8cd;
  }
  * { margin: 0; padding: 0; box-sizing: border-box; }
  html, body { width: 799px; height: 1200px; overflow: hidden; background: var(--orange-edge); }
  .cover {
    position: relative;
    width: 799px;
    height: 1200px;
    overflow: hidden;
    background: radial-gradient(circle at 50% 42%, var(--orange-core) 0%, var(--orange-mid) 45%, var(--orange-edge) 100%);
    font-family: "Open Sans", Arial, sans-serif;
  }
  .author {
    position: absolute;
    top: 12px;
    width: 100%;
    text-align: center;
    color: var(--yellow);
    font-size: 64px;
    font-weight: 400;
    letter-spacing: 1px;
  }
  .smile {
    position: absolute;
    left: 0;
    top: 0;
    filter: drop-shadow(0 0 10px rgba(255, 230, 80, 0.7));
  }
  .title {
    position: absolute;
    width: 100%;
    text-align: center;
    font-family: "Audiowide", "Arial Black", sans-serif;
    color: var(--white);
    text-shadow: 0 0 18px rgba(255, 255, 255, 0.75), 0 0 40px rgba(255, 240, 200, 0.5);
    line-height: 1;
  }
  .title-top { top: 298px; font-size: 150px; letter-spacing: -2px; }
  .title-mid {
    top: 420px;
    font-family: "Open Sans", Arial, sans-serif;
    font-weight: 800;
    font-size: 70px;
    color: var(--yellow);
    text-shadow: 0 0 14px rgba(255, 230, 80, 0.6);
  }
  .title-bottom { top: 518px; font-size: 140px; letter-spacing: -2px; }
  .subtitle {
    position: absolute;
    top: 815px;
    width: 100%;
    text-align: center;
    color: var(--white);
    font-size: 31px;
    font-weight: 700;
    letter-spacing: 0.5px;
  }
  .topic-band {
    position: absolute;
    left: 0;
    bottom: 0;
    width: 799px;
    height: 165px;
  }
  .topic-label {
    position: absolute;
    bottom: 34px;
    width: 100%;
    text-align: center;
    color: var(--band-text);
    font-size: 43px;
    font-weight: 400;
    white-space: nowrap;
  }
  .topic-label strong { font-weight: 800; }
</style>
</head>
<body>
<main class="cover">
  <p class="author">Marnie Calloway</p>

  <svg class="smile" width="799" height="1200" viewBox="0 0 799 1200" aria-hidden="true">
    <path d="M25 370 A375 355 0 0 0 775 370 A375 340 0 0 1 25 370 Z" fill="var(--smile-yellow)"/>
  </svg>

  <h1 class="title-group">
    <span class="title title-top">SMILING</span>
    <span class="title title-mid">opens every</span>
    <span class="title title-bottom">DOOR</span>
  </h1>

  <p class="subtitle">SO WHAT WAS THE QUESTION?</p>

  <svg class="topic-band" viewBox="0 0 799 165" preserveAspectRatio="none" aria-hidden="true">
    <path d="M0 18 Q400 -12 799 18 L799 165 L0 165 Z" fill="var(--band-pink)"/>
  </svg>
  <p class="topic-label"><strong>LAUGHTER</strong> AND <strong>BREAST CANCER</strong></p>
</main>
</body>
</html>
```